Electrical Safety Inspection for High End Customers

Flyer designed to advertise a 50 point electrical safety check service available from a recent start up electrician's firm in Auckland, New Zealand. I am a registered electrical inspector with 16 years experience.
Targeting high end customers, so I want the flyer to have a premium feel to it (glossy black background, etc). The final design should communicate peace of mind. The price will be $60 incl. GST
The checks included should be 1) Mains Cable 2)Mains entry point 3)Switchboard 4)Circuit protection correctly rated 5)Circuit protection operational 6)The main earthing system 7)Safety systems 8)Light fittings 9)Socket outlets 10)Deterioration of fittings 11)Deterioration of cabling 12)Compliance with current regulations
I have included a copy of the test sheet for reference. I have also included my logo and the qualified wiremen's guild of Ostravel, both of which must be present.
Target Market(s)
High end home owners
Industry/Entity Type
Electrician
Colors
Designer to choose colors to be used in the design.
Look and feel

```html
<!DOCTYPE html>
<html lang="en">
<head>
<meta charset="utf-8">
<title>Electrical Safety Matters</title>
<link rel="stylesheet" href="https://fonts.googleapis.com/css2?family=Fira+Sans:wght@500;600;700;800&display=swap">
<style>
  :root {
    --navy: #0f2d4a;
    --blue: #0d5a9a;
    --yellow: #e6e620;
    --white: #ffffff;
    --ink: #111418;
  }
  * { margin: 0; padding: 0; box-sizing: border-box; }
  html, body { width: 848px; height: 1200px; overflow: hidden; background: var(--navy); }
  .flyer {
    position: relative; width: 848px; height: 1200px; overflow: hidden;
    background: var(--navy); font-family: "Fira Sans", sans-serif; color: var(--white);
  }
  .icon-defs { position: absolute; width: 0; height: 0; }
  .hero-ring { position: absolute; left: 12px; top: 49px; }
  .guild-badge {
    position: absolute; left: 503px; top: 32px; width: 318px; height: 132px;
    background: var(--white); border-radius: 12px;
  }
  .headline {
    position: absolute; left: 484px; width: 364px; text-align: center;
    font-weight: 800; font-size: 64px; line-height: 1; letter-spacing: 2px; white-space: nowrap;
  }
  .headline--one { top: 214px; }
  .headline--two { top: 292px; }
  .headline--three { top: 374px; color: var(--yellow); }
  .price {
    position: absolute; left: 484px; width: 364px; top: 462px; text-align: center;
    font-weight: 700; font-size: 30px; line-height: 36px; white-space: nowrap;
  }
  .price .price-amount { color: var(--yellow); font-size: 40px; }
  .web-pill {
    position: absolute; left: 74px; top: 546px; width: 700px; height: 42px;
    background: var(--yellow); border-radius: 21px; text-align: center;
    color: var(--blue); font-weight: 700; font-size: 38px; line-height: 42px;
  }
  .email {
    position: absolute; right: 84px; top: 594px;
    color: var(--yellow); font-weight: 700; font-size: 31px; line-height: 36px;
  }
  .checks-title {
    position: absolute; left: 47px; top: 676px;
    font-weight: 700; font-size: 33px; line-height: 36px;
  }
  .check {
    position: absolute; display: flex; align-items: flex-start; gap: 12px;
    font-weight: 600; font-size: 21px; line-height: 28px; white-space: nowrap;
  }
  .check svg { flex: none; margin-top: -6px; }
  .call-band { position: absolute; left: 0; top: 1056px; }
  .call-icon { position: absolute; left: 21px; top: 1083px; }
  .call-text {
    position: absolute; left: 142px; top: 1086px;
    font-weight: 700; font-size: 31px; line-height: 38px;
  }
  .call-text .call-label { color: var(--yellow); }
  .brand {
    position: absolute; left: 548px; top: 1103px; display: flex; align-items: center; gap: 12px;
    color: var(--ink); font-weight: 800; font-size: 27px; line-height: 1.05; white-space: nowrap;
  }
  .brand-dot { width: 44px; height: 44px; border-radius: 50%; background: var(--ink); flex: none; }
</style>
</head>
<body>
<div class="flyer">

  <svg class="icon-defs" aria-hidden="true">
    <symbol id="tick" viewBox="0 0 42 42">
      <circle cx="21" cy="21" r="18" fill="none" stroke="#e6e620" stroke-width="3"/>
      <path d="M11 22 L18 30 L34 6" fill="none" stroke="#e6e620" stroke-width="4" stroke-linecap="round" stroke-linejoin="round"/>
    </symbol>
  </svg>

  <svg class="hero-ring" width="460" height="460" viewBox="0 0 460 460">
    <defs>
      <radialGradient id="photoTone" cx="45%" cy="45%" r="60%">
        <stop offset="0" stop-color="#c9a27f"/>
        <stop offset="0.45" stop-color="#8a8578"/>
        <stop offset="1" stop-color="#2a2d33"/>
      </radialGradient>
    </defs>
    <path d="M229 1 A229 229 0 0 0 229 459 Z" fill="#0d5a9a"/>
    <path d="M229 1 A229 229 0 0 1 229 459 Z" fill="#e6e620"/>
    <circle cx="229" cy="229" r="198" fill="url(#photoTone)" role="img" aria-label="Photo of an electrician's hands fitting a surge protector into a switchboard"/>
  </svg>

  <div class="guild-badge" role="img" aria-label="Member badge of the qualified wiremen's guild of Ostravel"></div>

  <div class="headline headline--one">ELECTRICAL</div>
  <div class="headline headline--two">SAFETY</div>
  <div class="headline headline--three">MATTERS</div>
  <div class="price"><span class="price-amount">$60</span> incl. GST</div>

  <div class="web-pill">www.websitename.com</div>
  <div class="email">emailaddress@email.com</div>

  <h2 class="checks-title">Main Safety Checks</h2>

  <!-- left column: checks 1 to 6 -->
  <div class="check" style="left:90px;top:732px;"><svg width="42" height="42"><use href="#tick"/></svg><span>Mains cable</span></div>
  <div class="check" style="left:131px;top:776px;"><svg width="42" height="42"><use href="#tick"/></svg><span>Mains entry point</span></div>
  <div class="check" style="left:90px;top:820px;"><svg width="42" height="42"><use href="#tick"/></svg><span>Switchboard</span></div>
  <div class="check" style="left:131px;top:864px;"><svg width="42" height="42"><use href="#tick"/></svg><span>Circuit protection<br>correctly rated</span></div>
  <div class="check" style="left:90px;top:932px;"><svg width="42" height="42"><use href="#tick"/></svg><span>Circuit protection<br>operational</span></div>
  <div class="check" style="left:131px;top:1000px;"><svg width="42" height="42"><use href="#tick"/></svg><span>The main earthing system</span></div>

  <!-- right column: checks 7 to 12 -->
  <div class="check" style="left:445px;top:732px;"><svg width="42" height="42"><use href="#tick"/></svg><span>Safety systems</span></div>
  <div class="check" style="left:486px;top:776px;"><svg width="42" height="42"><use href="#tick"/></svg><span>Light fittings</span></div>
  <div class="check" style="left:445px;top:820px;"><svg width="42" height="42"><use href="#tick"/></svg><span>Socket outlets</span></div>
  <div class="check" style="left:486px;top:864px;"><svg width="42" height="42"><use href="#tick"/></svg><span>Deterioration of fittings</span></div>
  <div class="check" style="left:445px;top:908px;"><svg width="42" height="42"><use href="#tick"/></svg><span>Deterioration of cabling</span></div>
  <div class="check" style="left:486px;top:952px;"><svg width="42" height="42"><use href="#tick"/></svg><span>Compliance with<br>current regulations</span></div>

  <svg class="call-band" width="848" height="144" viewBox="0 0 848 144">
    <rect width="848" height="144" fill="#0d5a9a"/>
    <polygon points="476,0 848,0 848,144 356,144" fill="#e6e620"/>
  </svg>

  <svg class="call-icon" width="88" height="88" viewBox="0 0 88 88">
    <circle cx="44" cy="44" r="41" fill="none" stroke="#ffffff" stroke-width="4"/>
    <path d="M31 24 c3 -2 6 0 7 3 l3 7 c1 2 0 4 -2 5 l-3 2 c2 5 6 9 11 11 l2 -3 c1 -2 3 -3 5 -2 l7 3 c3 1 5 4 3 7 l-3 4 c-2 3 -6 4 -10 3 c-14 -4 -25 -15 -29 -29 c-1 -4 0 -8 3 -10 z" fill="#ffffff"/>
    <path d="M48 26 a14 14 0 0 1 14 14" fill="none" stroke="#ffffff" stroke-width="3" stroke-linecap="round"/>
    <path d="M48 18 a22 22 0 0 1 22 22" fill="none" stroke="#ffffff" stroke-width="3" stroke-linecap="round"/>
  </svg>

  <div class="call-text">
    <div class="call-label">Call today</div>
    <div>(+123) 456 789</div>
  </div>

  <div class="brand">
    <span class="brand-dot"></span>
    <span>KESTREL LINE<br>ELECTRICAL</span>
  </div>

</div>
</body>
</html>
```